依頼詳細
今回作成するチラシは朝凪新報様へ折込む集客チラシの作成です。
しっかり集客ができる動線で作っていただきたいです。
「集客」という目標が最大限できれば、それ以外は求めません。
ターゲットは50代夫婦で子供は独立している方々です。お金は多少余裕があり、お庭の雑草対策に悩んでいる方へ最新技術の雑草の生えない人工芝をしっかりアピール(集客)したいです。
また、このチラシで集客するために、訪問見積もりご依頼いただいたお客様対象「限定15名 スパークリングワイン&スペシャルグラスプレゼント」キャンペーンをする予定です。
スパークリングワイン1本とスペシャルグラス2つプレゼントです。URLは以下の通りです。

https://www.kaimono-ichiba.example/[ルミオン]Lumion-フルートグラス-ステムレスグラスセット/dp/X00000001/

https://www.kaimono-ichiba.example/コルネット-厳選泡6本セット-750mlx6本ワインセット/dp/X00000002/
記載項目
社名:緑野芝生工房株式会社 / 電話:0120-555-318 / URL:tobu-lawn.example
サイズ
A4
ページ数
片面
希望イメージ
シンプル 複雑
単色 カラフル
暗い 明るい
日常 高級
遊び心 厳粛
未来的 伝統的
女性的 男性的
希望する色
緑系、集客さえできるチラシであれば何色を使っても正解です。
補足説明
必要な画像は弊社ホームページからいくらでも転用ください。
そのほか必要な画像は申しつけください。
追加でイメージをお伝えします。
新聞購読者が弊社折込チラシをパッと見て捨てないデザイン(インパクト・限定感・わかりやすさ)で、
電話番号大きくして「今すぐ電話しよう!」と自然とすぐ行動するような導線にしてください。
データを参考に添付します。
【仕様変更】

依頼内容の大幅な変更をお願いいたします。
キャンペーン「スパークリング ワイン・グラスプレゼント」は中止となりました。
もうすでにお取り組みされておられるランサーの方々には大変申し訳ございませんが、「スパークリングワイン・グラスプレゼント」は記載しないようお願いいたします。
また、その代わりにキャンペーン文言「もうすぐ完売! 【キャンペーンプラン】」というように訴求くださると助かります。(訴求のためでしたら追加で【急げ!】【期間限定!】等を追加で入れても問題ございません。)

「もうすぐ完売! 【キャンペーンプラン】」について補足いたします。
弊社では人工芝工事に「エコノミープラン」「ビジネスプラン」「ファーストクラスプラン」がありますが、
キャンペーンプランは通常の「ビジネスプラン」より約21,000円お安く工事が可能なプランです。
(上記のプランの説明を入れることは必須ということではございません。あくまでランサー様へご理解いただくため記載申し上げました。)
内容が大幅に変更となったこと、重ねてお詫び申し上げます。
■ 選んだ理由

訴求から問い合わせまでの動線と内容がよく、木になる人にも情報を提供していたため、デザインだけでなく、情報提供力に優れていたからです。

■ 提案者全員のお礼・コメント

ご提案くださりました全ての方々に、御礼申し上げます。
次回以降ももし可能でしたら優秀な皆様にまたご提案いただけますと嬉しい限りでございます。

```html
<!DOCTYPE html>
<html lang="ja">
<head>
<meta charset="utf-8">
<title>緑野芝生工房 人工芝 チラシ</title>
<link rel="stylesheet" href="https://fonts.googleapis.com/css2?family=Noto+Sans+JP:wght@400;500;700;900&family=Noto+Serif+JP:wght@500;700&display=swap">
<style>
  :root {
    --grass-dark: #2f6a1c;
    --grass-mid: #4f9a2c;
    --grass-light: #79bd43;
    --white: #ffffff;
    --ink: #1a1a1a;
    --orange: #e8720c;
    --gold: #c9a24a;
    --strip: #e9f1df;
    --pill: #e8720c;
  }
  * { margin: 0; padding: 0; box-sizing: border-box; }
  html, body { width: 849px; height: 1200px; overflow: hidden; }
  body { font-family: "Noto Sans JP", sans-serif; color: var(--ink); }
  .flyer { position: relative; width: 849px; height: 1200px; overflow: hidden; }
  .lawn-photo {
    position: absolute; inset: 0;
    background: radial-gradient(ellipse at 50% 40%, var(--grass-light) 0%, var(--grass-mid) 50%, var(--grass-dark) 100%);
  }
  .thought {
    position: absolute; left: 80px; top: 36px; width: 190px; height: 190px;
    border-radius: 50%; background: var(--white);
    display: flex; align-items: center; justify-content: center; text-align: center;
    color: var(--grass-mid); font-weight: 700; font-size: 20px; line-height: 1.35;
    white-space: nowrap;
  }
  .thought-dot { position: absolute; border-radius: 50%; background: var(--white); }
  .dot-1 { left: 150px; top: 238px; width: 30px; height: 30px; }
  .dot-2 { left: 138px; top: 280px; width: 19px; height: 19px; }
  .dot-3 { left: 130px; top: 310px; width: 12px; height: 12px; }
  .tagline {
    position: absolute; right: 32px; top: 40px;
    writing-mode: vertical-rl; font-family: "Noto Serif JP", serif; font-weight: 700;
    font-size: 42px; letter-spacing: 0.08em; color: var(--white);
    text-shadow: 0 0 6px rgba(0,0,0,0.35);
  }
  .message-box {
    position: absolute; left: 270px; top: 420px; width: 322px; height: 352px;
    background: var(--white); padding: 26px 20px 0;
  }
  .headline { font-size: 28px; font-weight: 900; line-height: 1.45; white-space: nowrap; }
  .lead { margin-top: 20px; color: var(--orange); font-weight: 700; font-size: 15.5px; line-height: 1.6; white-space: nowrap; }
  .award-badge { display: block; margin: 20px auto 0; width: 240px; height: 66px; }
  .support { margin-top: 18px; font-size: 12.5px; font-weight: 700; line-height: 1.65; white-space: nowrap; }
  .brand { position: absolute; left: 0; right: 0; top: 800px; text-align: center; color: var(--white); }
  .brand-mark { display: block; width: 54px; height: 62px; margin: 0 auto; border: 3px solid var(--white); }
  .brand-name { margin-top: 8px; font-size: 30px; font-weight: 700; letter-spacing: 0.06em; }
  .brand-url { font-size: 22px; font-weight: 700; }
  .contact-label { position: absolute; left: 50px; top: 1040px; color: var(--white); font-weight: 700; font-size: 18px; line-height: 1.3; }
  .phone { position: absolute; left: 262px; top: 1012px; display: flex; align-items: center; color: var(--white); font-weight: 900; font-size: 64px; line-height: 1.2; }
  .phone svg { width: 50px; height: 50px; margin-right: 8px; }
  .address { position: absolute; left: 270px; top: 1104px; color: var(--white); font-size: 12px; }
  .campaign-strip {
    position: absolute; left: 0; right: 0; bottom: 0; height: 50px; background: var(--strip);
    display: flex; align-items: center; padding-left: 40px;
  }
  .pill { background: var(--pill); color: var(--white); font-size: 13px; font-weight: 700; border-radius: 14px; padding: 3px 14px; }
  .campaign-text { margin-left: 18px; font-size: 20px; font-weight: 900; color: var(--orange); }
</style>
</head>
<body>
<div class="flyer">
  <div class="lawn-photo" role="img" aria-label="一面に広がる緑の人工芝の写真"></div>

  <div class="thought">第6世代の<br>人工芝は<br>リアルな<br>芝の感触です。</div>
  <span class="thought-dot dot-1"></span>
  <span class="thought-dot dot-2"></span>
  <span class="thought-dot dot-3"></span>

  <p class="tagline">芝生のある生活を、これからも「ずっと」。</p>

  <section class="message-box">
    <h1 class="headline">雑草が生えない。<br>10年間の長期寿命。</h1>
    <p class="lead">人工芝の価格を業界平均より抑え、<br>最高品質の人工芝工事を提供します。</p>
    <svg class="award-badge" viewBox="0 0 240 66" aria-hidden="true">
      <rect x="0" y="0" width="240" height="66" fill="var(--gold)"/>
    </svg>
    <p class="support">安心・安全の施工技術と充実した<br>アフターサポートで喜んでいただいております。</p>
  </section>

  <div class="brand">
    <span class="brand-mark"></span>
    <p class="brand-name">緑野芝生工房</p>
    <p class="brand-url">www.tobu-lawn.example</p>
  </div>

  <p class="contact-label">ご相談・お問合せは<br>コチラまで</p>
  <p class="phone">
    <svg viewBox="0 0 24 24" aria-hidden="true"><path fill="#fff" d="M6.6 10.8a15.1 15.1 0 0 0 6.6 6.6l2.2-2.2a1 1 0 0 1 1-.25 11.4 11.4 0 0 0 3.6.57 1 1 0 0 1 1 1V20a1 1 0 0 1-1 1A17 17 0 0 1 3 4a1 1 0 0 1 1-1h3.5a1 1 0 0 1 1 1c0 1.25.2 2.45.57 3.57a1 1 0 0 1-.25 1z"/></svg>
    0120-555-318
  </p>
  <p class="address">緑野芝生工房株式会社　〒000-0000 緑野市芝生町1-2-3</p>

  <div class="campaign-strip">
    <span class="pill">急げ!もうすぐ完売</span>
    <span class="campaign-text">おトクな「キャンペーンプラン」実施中!</span>
  </div>
</div>
</body>
</html>
```